Build a new Capability Statement for a labour support and maintenance company

Hi Everyone,
We wish to update our capability statement. Attached is a powerpoint that has the key ideas with random pictures we would like in the document. I have also attached a competitors document as a sample of the things we like. This document is being sent to our entire client base which includes Tier 1 mining companies like Vela Corran & KQS

Target Market(s)

Mining Companies

Industry/Entity Type

Mining

Colors

Designer to choose colors to be used in the design.

```html
<!DOCTYPE html>
<html lang="en">
<head>
<meta charset="utf-8">
<title>Redgate Capability Statement</title>
<link rel="stylesheet" href="https://fonts.googleapis.com/css2?family=Montserrat:wght@600;700&family=Didact+Gothic&family=Roboto+Condensed:ital,wght@1,700&display=swap">
<style>
  :root {
    --backdrop: #e4e4e6;
    --paper: #ffffff;
    --gold: #d6a93a;
    --gold-deep: #c4922a;
    --gold-soft: rgba(214, 169, 58, 0.78);
    --charcoal: #2f2f30;
    --ink: #262626;
    --body: #3c3c3c;
  }
  html, body {
    margin: 0;
    padding: 0;
    width: 1200px;
    height: 4091px;
    overflow: hidden;
    background: var(--backdrop);
  }
  .canvas {
    position: relative;
    width: 1200px;
    height: 4091px;
  }
  .spread {
    position: absolute;
    left: 229px;
    width: 742px;
    height: 523px;
    background: var(--paper);
    box-shadow: 0 8px 24px rgba(0, 0, 0, 0.12);
  }
  .spread svg { display: block; width: 100%; height: 100%; }
  .spread--cover { top: 2846px; }
  .spread--inside { top: 3439px; }

  .brand-name { font-family: "Montserrat", sans-serif; font-weight: 700; fill: var(--ink); }
  .title { font-family: "Didact Gothic", sans-serif; fill: var(--ink); }
  .title--main { font-family: "Montserrat", sans-serif; font-weight: 700; }
  .contact-head { font-family: "Montserrat", sans-serif; font-weight: 600; fill: var(--gold); }
  .contact-line, .web-line { font-family: "Didact Gothic", sans-serif; fill: var(--body); }
  .section-head { font-family: "Montserrat", sans-serif; font-weight: 700; }
  .section-head--gold { fill: var(--gold); }
  .section-head--dark { fill: var(--ink); }
  .intro-line { font-family: "Didact Gothic", sans-serif; fill: #ffffff; }
  .body-copy { font-family: "Didact Gothic", sans-serif; fill: var(--body); }
  .client-list { font-family: "Roboto Condensed", sans-serif; font-style: italic; font-weight: 700; fill: var(--ink); }
  .icon { fill: var(--gold); }
</style>
</head>
<body>
<main class="canvas">

  <section class="spread spread--cover">
    <svg viewBox="0 0 468 330" xmlns="http://www.w3.org/2000/svg">
      <defs>
        <linearGradient id="siteGrey" x1="0" y1="0" x2="0" y2="1">
          <stop offset="0" stop-color="#6a6a6a"/>
          <stop offset="0.6" stop-color="#4d4d4d"/>
          <stop offset="1" stop-color="#8c8c8c"/>
        </linearGradient>
        <linearGradient id="loaderPhoto" x1="0" y1="0" x2="1" y2="1">
          <stop offset="0" stop-color="#4f8fd6"/>
          <stop offset="0.35" stop-color="#c9b27a"/>
          <stop offset="0.7" stop-color="#8a7452"/>
          <stop offset="1" stop-color="#b79c74"/>
        </linearGradient>
      </defs>

      <rect width="468" height="330" fill="var(--paper)"/>

      <polygon role="img" aria-label="Greyscale photo of a service ute parked on a mine site"
               points="0,0 90,0 200,240 0,170" fill="url(#siteGrey)"/>

      <polygon role="img" aria-label="Faded photo of a large excavator under a gold overlay"
               points="76,0 256,0 256,330 170,330" fill="var(--gold)"/>
      <polygon points="76,0 150,0 190,230 120,130" fill="var(--gold-deep)" opacity="0.35"/>

      <polygon role="img" aria-label="Photo of a yellow wheel loader on a gravel mine site"
               points="301,112 468,137 468,297 236,297 256,170" fill="url(#loaderPhoto)"/>
      <polygon points="256,170 320,220 290,297 236,297" fill="var(--gold-soft)"/>

      <!-- Back page -->
      <text class="contact-head" x="20" y="251" font-size="6.2">GET IN TOUCH!</text>
      <path class="icon" d="M21 261.2c.6 1.4 1.6 2.4 3 3l1-1 1.3.6-.4 1.4c-2.6-.2-4.8-2.4-5-5l1.4-.4.6 1.3z"/>
      <text class="contact-line" x="30" y="265" font-size="4.6">0400 123 456</text>
      <path class="icon" d="M23.2 269.5a1.9 1.9 0 0 1 1.9 1.9c0 1.4-1.9 3.4-1.9 3.4s-1.9-2-1.9-3.4a1.9 1.9 0 0 1 1.9-1.9z"/>
      <text class="contact-line" x="30" y="273" font-size="4.6">PO Box 4120, Bayview</text>
      <text class="contact-line" x="30" y="278.5" font-size="4.6">North WA 6099</text>
      <circle class="icon" cx="23.2" cy="284.4" r="1.8"/>
      <text class="contact-line" x="30" y="286" font-size="4.6">www.redgatemc.com.au</text>

      <text class="brand-name" x="136" y="291" font-size="14">Redgate</text>

      <!-- Front page -->
      <text class="brand-name" x="440" y="40" font-size="16" text-anchor="end">Redgate</text>
      <text class="title title--main" x="440" y="95" font-size="18.5" text-anchor="end">Capability</text>
      <text class="title" x="440" y="108" font-size="9" text-anchor="end">Statement</text>

      <circle class="icon" cx="259" cy="300" r="1.8"/>
      <text class="web-line" x="265" y="302" font-size="4.6">www.redgatemc.com.au</text>
    </svg>
  </section>

  <section class="spread spread--inside">
    <svg viewBox="0 0 468 330" xmlns="http://www.w3.org/2000/svg">
      <defs>
        <linearGradient id="aerialPhoto" x1="0" y1="0" x2="1" y2="1">
          <stop offset="0" stop-color="#b5876a"/>
          <stop offset="0.5" stop-color="#9b4b32"/>
          <stop offset="1" stop-color="#c98e6c"/>
        </linearGradient>
        <linearGradient id="excavatorPhoto" x1="0" y1="0" x2="0" y2="1">
          <stop offset="0" stop-color="#ffffff" stop-opacity="0"/>
          <stop offset="0.35" stop-color="#d8dde4"/>
          <stop offset="0.65" stop-color="#c8743a"/>
          <stop offset="1" stop-color="#e6cfa6"/>
        </linearGradient>
        <linearGradient id="thumbA" x1="0" y1="0" x2="0" y2="1">
          <stop offset="0" stop-color="#9aa2a8"/><stop offset="1" stop-color="#8a5a3e"/>
        </linearGradient>
        <linearGradient id="thumbB" x1="0" y1="0" x2="1" y2="1">
          <stop offset="0" stop-color="#2b2b2b"/><stop offset="1" stop-color="#c9a23a"/>
        </linearGradient>
        <linearGradient id="thumbC" x1="0" y1="0" x2="0" y2="1">
          <stop offset="0" stop-color="#8f949a"/><stop offset="1" stop-color="#5c5f63"/>
        </linearGradient>
      </defs>

      <rect width="468" height="330" fill="var(--paper)"/>

      <!-- Left page -->
      <rect x="0" y="0" width="138" height="92" fill="var(--charcoal)"/>
      <polygon role="img" aria-label="Aerial photo of a red-earth mine haul road"
               points="138,0 234,0 234,92 138,92" fill="url(#aerialPhoto)"/>
      <text class="section-head section-head--gold" x="20" y="32" font-size="11">Company Profile</text>
      <text class="intro-line" font-size="4.6">
        <tspan x="20" y="44">We believe our repeat clients</tspan>
        <tspan x="20" y="50">are evidence of our commitment</tspan>
        <tspan x="20" y="56">to excellence</tspan>
      </text>

      <text class="body-copy" font-size="4.4">
        <tspan x="20" y="118">Redgate Mining and Civil Pty Ltd (Redgate) have a fully mobile workforce</tspan>
        <tspan x="20" y="124">as well as an extensive schedule of plant and equipment to support any</tspan>
        <tspan x="20" y="130">project.</tspan>
        <tspan x="20" y="142">We are a family owned WA business backed by a loyal team of motivated</tspan>
        <tspan x="20" y="148">and skilled individuals who are always available to meet your needs.</tspan>
        <tspan x="20" y="160">We understand downtime can be costly to companies which is why Redgate</tspan>
        <tspan x="20" y="166">is committed to providing cost effective and efficient solutions for your</tspan>
        <tspan x="20" y="172">business. Project objectives are always met with outstanding client service</tspan>
        <tspan x="20" y="178">and field excellence.</tspan>
        <tspan x="20" y="190">Since our inception in 2011 clients who engage Redgate have become confi-</tspan>
        <tspan x="20" y="196">dent that they will receive professional, proficient and qualified people</tspan>
        <tspan x="20" y="202">and plant on their jobs.</tspan>
      </text>

      <text class="client-list" font-size="6">
        <tspan x="20" y="250">Some past and present clients include</tspan>
        <tspan x="20" y="258">Vela Corran, Stonevale, Ferrock Iron, Meridian</tspan>
        <tspan x="20" y="266">Construction Pty Ltd, Corvel Industries,</tspan>
        <tspan x="20" y="274">Ashgrove Mining, Tallis Mining,</tspan>
        <tspan x="20" y="282">Norda Mining &amp; Norda Civil</tspan>
      </text>

      <text class="brand-name" x="158" y="286" font-size="13">Redgate</text>

      <!-- Right page -->
      <text class="section-head section-head--dark" font-size="10">
        <tspan x="253" y="30">Redgate Labour Support &amp;</tspan>
        <tspan x="253" y="43">Rapid Response</tspan>
      </text>
      <text class="body-copy" font-size="4.4">
        <tspan x="253" y="66">Redgate is available for rapid response, onsite support and maintenance</tspan>
        <tspan x="253" y="72">24/7 to keep your business and equipment powering. We offer full me-</tspan>
        <tspan x="253" y="78">chanical repairs, component rebuilds and exchanges, digger support</tspan>
        <tspan x="253" y="84">and mining vehicle specification fit outs. Redgate can source cost effective</tspan>
        <tspan x="253" y="90">parts quality parts and OEM standards.</tspan>
        <tspan x="253" y="102">Our dedicated team will ensure all projects are completed within speci-</tspan>
        <tspan x="253" y="108">fied timeframes ensuring the highest level of workmanship and safety is</tspan>
        <tspan x="253" y="114">maintained</tspan>
      </text>

      <rect role="img" aria-label="Photo of a service ute on site" x="253" y="158" width="56" height="38" fill="url(#thumbA)"/>
      <rect role="img" aria-label="Photo of yellow plant in a workshop at night" x="318" y="158" width="56" height="38" fill="url(#thumbB)"/>
      <rect role="img" aria-label="Photo of a service truck in a workshop" x="383" y="158" width="56" height="38" fill="url(#thumbC)"/>

      <rect role="img" aria-label="Photo of an orange excavator with a city skyline at sunset"
            x="234" y="200" width="234" height="130" fill="url(#excavatorPhoto)"/>
      <polygon points="290,330 468,268 468,330" fill="var(--gold)"/>
      <polygon points="350,330 468,290 468,330" fill="var(--gold-deep)" opacity="0.5"/>
    </svg>
  </section>

</main>
</body>
</html>
```